Rondo Brisk Painting, Eco and Non toxic painting client information brochure.

Rondo brisk painting is a painting company that specialises in eco and non toxic paints. This brochure will be left with the client after the initial meeting to explain about my business and hopefully win the job. By reading the text i have provided (see attachment) you can get a better understanding of what we do.
The brochure should be fresh and clean looking, complimenting the Rondo Brisk Painting logo and the text provided.
This will be printed onto a recycled paper.
Text and font must clear and easy to read.

Please have a look at my web page. I will be redoing this soon as well but this will give you some ideas of where I'm at.

Would like some picture but not sure what.
I have attached some pics but they don't have to be use

Hi peeps,

Thanks for all the great designs and sorry i haven't got back to you sooner.
been a bit busy.
Tomorrow i hope to be able to sit down and have a good look at what everybody has done.
Thanks again i really appreciate the effort.

kind regards gerald 

hi designers,

Just sat down and had a good look at the designs sent in and there are some crackers.
Its going to be very difficult to choose. I have only 1 day left before it closes so ill wait till then to see if there are any more submissions come in then ill get back to everybody.
Thanks again for your time and effort.

kind regards gerald 

Hi too all you designers that have worked on my project. 

I am always amazed at all the different designs that come through. Super work guys and girls. 
I have narrowed it down to a couple of designs.
Ill be making the decision tonight.
Thanks again to you all and i really appreciate all the hard work.
I will be doing another brochure in the future for more architecture / builder focus and there were a few designs that would work perfectly for this.

Kinds regards gerald  

Target Market(s)

The work we do is mainly residential repaints, family homes
Mostly I am dealing with the wife of the family or female designers/architects

Industry/Entity Type

Painting

Requirements
Must have
• Company logo, either white or black version what ever suits best.
Text that has been provided.
Brochure will be 1 page A 4, folded into 3 parts both sides.
Front page must have logo and
SPECIALSING IN:
NON TOXIC
ECO FRIENDLY &
HEAT REFLECTIVE PAINTS
Phone 041 862 9147
Painting@rondobrisk.biz
www.rondobrisk.biz

```html
<!DOCTYPE html>
<html lang="en">
<head>
<meta charset="utf-8">
<title>Rondo Brisk Painting – Client Brochure</title>
<link rel="stylesheet" href="https://fonts.googleapis.com/css2?family=Archivo+Black&family=Arimo:wght@400;700&display=swap">
<style>
  :root {
    --backdrop: #e4e4e4;
    --paper: #e8f3d2;
    --paper-light: #f4f9ea;
    --leaf-green: #5c9b2c;
    --deep-green: #3f7a1e;
    --ink: #2b2b2b;
    --tox-blue: #2c4fb0;
    --eco-green: #3f9a2a;
    --heat-red: #d2262a;
    --paints-black: #1a1a1a;
    --fold-line: rgba(80, 110, 50, 0.18);
  }
  * { box-sizing: border-box; margin: 0; padding: 0; }
  html, body {
    width: 1200px; height: 931px; overflow: hidden;
    background: var(--backdrop);
  }
  .canvas {
    width: 1200px; height: 931px;
    display: flex; align-items: center; justify-content: center;
  }
  .brochure {
    display: flex;
    width: 1080px; height: 700px;
    box-shadow: 0 18px 40px rgba(0,0,0,0.18);
  }
  .panel {
    width: 360px; height: 700px;
    background: linear-gradient(160deg, var(--paper-light), var(--paper));
    border-right: 1px solid var(--fold-line);
    position: relative;
  }
  .panel:last-child { border-right: none; }

  /* Inside info panel */
  .info { padding: 46px 34px; }
  .info h2 {
    font-family: "Archivo Black", sans-serif;
    color: var(--leaf-green);
    font-size: 19px; letter-spacing: 0.5px;
    text-transform: uppercase; line-height: 1.2;
    margin-bottom: 12px;
  }
  .info p {
    font-family: "Arimo", sans-serif;
    color: var(--ink);
    font-size: 13.5px; line-height: 1.5;
    text-align: justify;
    margin-bottom: 26px;
  }
  .info .tin-art {
    position: absolute; left: 40px; bottom: 40px;
    width: 150px; height: 130px; border-radius: 50%;
    background: radial-gradient(circle at 50% 50%, #6f9a35 0%, #8fb356 45%, rgba(160,190,110,0) 72%);
  }

  /* Photo panel */
  .gallery { padding: 40px 30px; display: flex; flex-direction: column; gap: 20px; }
  .photo { flex: 1; border: 4px solid #fff; box-shadow: 0 3px 8px rgba(0,0,0,0.12); }
  .photo.rooms { background: linear-gradient(135deg, #c9b08a, #e9dcc4 55%, #9c7a56); }
  .photo.house { background: linear-gradient(180deg, #8fb6dc, #dfe7ee 45%, #b08b63); }
  .photo.colour { background: linear-gradient(120deg, #d3452c, #e98a2a 40%, #f2c84b 70%, #6aa33a); }

  /* Cover */
  .cover { padding: 60px 34px 0; }
  .specials {
    font-family: "Archivo Black", sans-serif;
    font-size: 30px; line-height: 1.12;
    text-transform: uppercase; text-align: right;
  }
  .specials .tox { color: var(--tox-blue); }
  .specials .eco { color: var(--eco-green); }
  .specials .heat { color: var(--heat-red); }
  .specials .paints { color: var(--paints-black); }
  .pots-art {
    width: 250px; height: 250px; margin: 34px auto 0;
    border-radius: 50%;
    background: radial-gradient(circle, #f2e23a 0 18%, #7b3cb0 19% 30%, #e2342b 31% 44%, #35a7d6 45% 58%, #3fae3a 59% 72%, rgba(232,243,210,0) 73%);
  }
  .brand {
    position: absolute; left: 34px; bottom: 52px;
    display: flex; align-items: center; gap: 12px;
  }
  .brand-mark { width: 30px; height: 30px; background: var(--leaf-green); }
  .brand-name {
    font-family: "Archivo Black", sans-serif;
    font-size: 24px; color: var(--paints-black);
    text-transform: uppercase; line-height: 1.05;
  }
</style>
</head>
<body>
<main class="canvas">
  <section class="brochure">
    <article class="panel info">
      <h2>Hiring a Professional</h2>
      <p>Hiring a professional painter is more than a quick decision. We bring skill, care and the right preparation to every room, so your home looks fresh, lasts longer and the job runs smoothly from first visit to final coat.</p>
      <h2>Going Green</h2>
      <p>We help you make smart choices about paint, offering low odour and low VOC products that protect your family and the planet while still giving a strong, lasting finish.</p>
      <h2>VOCs = Volatile Organic Compounds</h2>
      <p>VOCs are chemicals released into the air as ordinary paint dries. They can cause headaches, irritation and poor indoor air for days after painting. Non toxic and eco friendly paints keep these levels very low, so your rooms are safe to use sooner and the air inside your home stays clean.</p>
      <div class="tin-art" role="img" aria-label="Open tin of green paint with a brush and splashes"></div>
    </article>

    <article class="panel gallery">
      <div class="photo rooms" role="img" aria-label="Photo of a freshly painted living room"></div>
      <div class="photo house" role="img" aria-label="Photo of a repainted family home exterior"></div>
      <div class="photo colour" role="img" aria-label="Photo of colourful paint samples"></div>
    </article>

    <article class="panel cover">
      <h1 class="specials">
        <span class="tox">Non Toxic</span><br>
        <span class="eco">Eco Friendly &amp;</span><br>
        <span class="heat">Heat Reflective</span><br>
        <span class="paints">Paints</span>
      </h1>
      <div class="pots-art" role="img" aria-label="Illustration of paint pots arranged as a flower with a green stem and leaves"></div>
      <div class="brand">
        <span class="brand-mark"></span>
        <span class="brand-name">Rondo Brisk<br>Painting</span>
      </div>
    </article>
  </section>
</main>
</body>
</html>
```